依頼詳細
・余白のある、落ち着いたデザインを希望です。
・以下参考サイトのような色味(キーカラー)を希望です。
(デザインは極端に類似しないことが望ましい)
- https://rinpa-kissa.jp/
- https://hamonoya.com/
・サイトのメニューは
-ごあいさつ
-会社案内・沿革
-事業内容
-納入実績
-お問い合わせ
-みなせのものづくり(ブログ)
-ネットショップ
となる予定です。
この度は、「TOPページのデザイン」と、上記「下層ページのベースデザイン」を依頼いたします。
・レスポンシブでスマートフォンにも対応させます。
・TOPページにはNEWS(お知らせ)欄が入る予定です。
・最終的に当方でWordPressにて構築します。
・参考サイトのイメージにとらわれない自由なデザインでもOKです。
ぜひ様々なアイデアをご提案下さい。
サイトURL
ページ数
2ページ
希望イメージ
シンプル 複雑
単色 カラフル
暗い 明るい
日常 高級
遊び心 厳粛
未来的 伝統的
女性的 男性的
希望する色
茶系、背景は白でお願いいたします。
納品ファイル
• 高解像度JPG (.jpg)
• イラストレーター形式 (.ai)
• フォトショップ形式 (.psd)
• PNG形式 (.png)
補足説明
資料と素材写真を添付いたします。
写真は今後差し替え予定なのでダミーとしてお使いください。

素材画像で購入が必要なものがある場合、「Pexel Vault (https://vault.pexelmart.com/jp/)」より選定下さい。当方で購入しますので、ご提案の際はカンプ画像を利用いただき、採用後には素材のURL or ファイル番号をお伝えいただきます。

その他ご不明な点がございましたら、お気軽にご連絡下さい。

シンプルで飽きの来ないデザインをクライアント様が気に入りました。

この度は本当にたくさんのご提案をいただきましてまことにありがとうございました。
どのデザインも素敵で、選ぶのに時間がかかりまして申し訳ございませんでした。
またの機会がございましたらご提案ください。改めて御礼申し上げます。

```html
<!DOCTYPE html>
<html lang="ja">
<head>
<meta charset="utf-8">
<title>木型みなせ</title>
<link rel="stylesheet" href="https://fonts.googleapis.com/css2?family=Shippori+Mincho:wght@400;600&family=Noto+Sans+JP:wght@300;400&display=swap">
<style>
:root{
  --brown:#c39463;
  --brown-dark:#8a6440;
  --ink:#4a4340;
  --muted:#8c8480;
  --line:#d9cfc6;
  --paper:#ffffff;
  --wood:#c9a884;
}
*{box-sizing:border-box;margin:0;padding:0}
html,body{width:1200px;height:2432px;overflow:hidden;background:var(--paper)}
body{position:relative;font-family:"Noto Sans JP",sans-serif;color:var(--ink);font-size:13px;line-height:1.9}
.serif{font-family:"Shippori Mincho",serif}
.logo{position:absolute;top:6px;left:0;width:1200px;text-align:center}
.logo-name{font-family:"Shippori Mincho",serif;font-size:22px;color:var(--brown-dark);letter-spacing:4px;line-height:1.3}
.logo-sub{font-size:9px;color:var(--muted);letter-spacing:2px}
.side-social{position:absolute;right:0;top:320px;width:24px;background:var(--brown-dark);padding:6px 5px;display:flex;flex-direction:column;gap:8px}
.side-social span{display:block;width:14px;height:14px;background:#fff;border-radius:2px}
.hero{position:absolute;top:52px;left:120px;width:1020px;height:310px;background:linear-gradient(120deg,#e8d9c4,#c9a884 55%,#a57d57)}
.hero-copy{position:absolute;right:60px;top:130px;color:#fff;font-family:"Shippori Mincho",serif;font-size:16px;letter-spacing:3px}
.gnav{position:absolute;top:398px;left:120px;width:1020px;display:flex;border-top:1px solid var(--line);border-bottom:1px solid var(--line)}
.gnav a{flex:1;text-align:center;font-size:12px;color:var(--ink);text-decoration:none;padding:8px 0;border-left:1px solid var(--line)}
.gnav a:first-child{border-left:none}
.vline{position:absolute;width:1px;background:var(--line)}
.greet-photo{position:absolute;top:580px;left:0;width:700px;height:300px;background:linear-gradient(135deg,#7a4e30,#b07a4f 60%,#d3ab80)}
.greet{position:absolute;top:600px;left:780px;width:360px}
h2{font-family:"Shippori Mincho",serif;font-weight:400;font-size:24px;color:var(--brown-dark);letter-spacing:3px}
.greet p{margin-top:14px;font-size:12px;color:var(--muted)}
.biz-title{position:absolute;top:990px;left:0;width:1200px;text-align:center}
.biz{position:absolute;left:160px;width:440px;text-align:center}
.biz.r{left:620px}
.biz h3{font-family:"Shippori Mincho",serif;font-weight:400;font-size:15px;color:var(--ink);margin-bottom:8px}
.biz p{font-size:11.5px;color:var(--muted);text-align:left}
.btn{position:absolute;display:flex;align-items:center;justify-content:center;gap:10px;background:var(--brown);color:#fff;font-size:13px;letter-spacing:2px}
.works-title{position:absolute;top:1570px;left:128px}
.works{position:absolute;top:1620px;left:128px;width:1012px;display:grid;grid-template-columns:repeat(6,1fr);gap:20px 14px}
.works div{height:140px}
.news{position:absolute;top:2060px;left:128px;width:640px;text-align:center}
.news ul{list-style:none;margin-top:26px;text-align:left;padding-left:120px}
.news li{font-size:12px;color:var(--muted);padding:8px 0;border-bottom:1px solid #eee}
.news li b{font-weight:400;color:var(--brown-dark);margin-right:20px}
.company{position:absolute;top:2080px;left:800px;width:340px;height:320px;background:var(--brown);color:#fff;padding:150px 30px 0;font-size:11px;line-height:1.9}
.company strong{display:block;font-family:"Shippori Mincho",serif;font-weight:400;font-size:14px;margin-bottom:4px}
.fnav{position:absolute;top:2404px;left:120px;width:1020px;display:flex;justify-content:space-between;font-size:10px;color:var(--muted)}
</style>
</head>
<body>
<header class="logo">
  <div class="logo-name">木型みなせ</div>
  <div class="logo-sub">MINASE WOODEN MOLD WORKS</div>
</header>
<div class="side-social"><span></span><span></span></div>

<div class="hero" role="img" aria-label="木製の押し型と木型を並べた写真">
  <div class="hero-copy">一点モノの木型を、職人の手で。</div>
</div>

<nav class="gnav">
  <a>ごあいさつ</a><a>会社案内・沿革</a><a>事業内容</a><a>納入実績</a><a>みなせのものづくり</a><a>ネットショップ</a><a>お問い合わせ</a>
</nav>
<div class="vline" style="left:740px;top:434px;height:90px"></div>

<div class="greet-photo" role="img" aria-label="文字を彫り込んだ木の看板の写真"></div>
<section class="greet">
  <h2>ごあいさつ</h2>
  <p>木型みなせは、創業以来一貫して木型の製作に携わってまいりました。菓子型や押し型など、用途に合わせた一点ものを手作業で仕上げています。</p>
  <p>長年培った技術と新しい道具を組み合わせ、お客様のご要望に丁寧にお応えします。小さなご相談でもお気軽にお声がけください。</p>
  <p>これからも木の温もりを大切に、ものづくりを続けてまいります。</p>
</section>
<div class="vline" style="left:600px;top:900px;height:80px"></div>

<div class="biz-title"><h2>みなせの事業</h2></div>
<section class="biz" style="top:1050px"><h3>技術紹介</h3><p>職人の手彫りと機械加工を組み合わせ、細かな模様まで正確に再現します。素材選びから仕上げまで一貫して対応いたします。</p></section>
<section class="biz r" style="top:1050px"><h3>木型の作成</h3><p>和菓子や料理の型、工芸用の型など、用途に合わせた木型を製作します。少量からのご注文にも対応いたします。</p></section>
<section class="biz" style="top:1200px"><h3>テーマ素材制作</h3><p>ロゴや文字を木に彫り込み、記念品や看板として仕上げます。データ入稿や手描きの原稿からも製作が可能です。</p></section>
<section class="biz r" style="top:1200px"><h3>新規デザイン</h3><p>図案の作成からご提案いたします。イメージを伺いながら、形と彫りの深さを一緒に決めていきます。</p></section>
<section class="biz" style="top:1350px"><h3>押し型自由</h3><p>既存の型の修理や複製も承ります。お気軽にご相談ください。</p></section>
<div class="btn" style="top:1360px;left:620px;width:440px;height:90px">もっと見る
  <svg width="24" height="8" viewBox="0 0 24 8"><path d="M0 6H22L17 1" fill="none" stroke="#fff"/></svg></div>

<div class="works-title"><h2>納入実績</h2></div>
<section class="works">
  <div role="img" aria-label="木箱の実績写真" style="background:linear-gradient(#8a5a3a,#c69b72)"></div>
  <div role="img" aria-label="菓子型の実績写真" style="background:linear-gradient(#c9a47e,#e8d6bf)"></div>
  <div role="img" aria-label="焼印の実績写真" style="background:linear-gradient(#e6ddd3,#b08a67)"></div>
  <div role="img" aria-label="木札の実績写真" style="background:linear-gradient(#5a3b2a,#9b7252)"></div>
  <div role="img" aria-label="押し型の実績写真" style="background:linear-gradient(#d8c1a2,#a98462)"></div>
  <div role="img" aria-label="木のへらの実績写真" style="background:linear-gradient(#f2e7d8,#d1a56b)"></div>
  <div role="img" aria-label="白い型の実績写真" style="background:linear-gradient(#f4f2ef,#cfc7bf)"></div>
  <div role="img" aria-label="丸型の実績写真" style="background:linear-gradient(#9c6e4a,#d9b993)"></div>
  <div role="img" aria-label="青い製品の実績写真" style="background:linear-gradient(#3b5f9a,#8ea7cc)"></div>
  <div role="img" aria-label="工房の実績写真" style="background:linear-gradient(#6b5a55,#b09a8e)"></div>
  <div role="img" aria-label="木製品の実績写真" style="background:linear-gradient(#b98a5c,#e2c8a4)"></div>
  <div class="btn" style="position:static">もっと見る</div>
</section>

<section class="news">
  <h2>おしらせ</h2>
  <ul>
    <li><b>2024.05.12</b>ホームページを公開しました</li>
    <li><b>2024.04.28</b>ゴールデンウィーク休業のお知らせ</li>
    <li><b>2024.04.02</b>新しい押し型の受付を開始しました</li>
    <li><b>2024.03.15</b>工房見学のご案内を更新しました</li>
  </ul>
</section>
<div class="company">
  <strong>有限会社みなせ木工</strong>
  〒000-0000<br>架空県みなせ市木工町1-2-3<br>TEL 000-000-0000
</div>

<footer class="fnav">
  <span>ごあいさつ</span><span>会社案内・沿革</span><span>事業内容</span><span>納入実績</span><span>みなせのものづくり</span><span>ネットショップ</span><span>お問い合わせ</span>
</footer>
</body>
</html>
```